wedding DJ & Lighting entertainment

We are a DJ and Lighting production company. We specialize mainly in wedding entertainment. I've attached my old postcard in the image folder, however, i would like something new and updated. You can use the same bullet points from the front page, but i would like to have a cleaner look on the front. I'd like to have one large image on the front side and smaller images on the back side. I'd also like to have some text below the logo. I'd like it to say DJ * Lighting * Audio/Visual. I'd also like to have the phrase "Celebrate with Style"

Target Market(s)

weddings, private events, women

Industry/Entity Type

It Company

Font styles to use
Sans Serif
Script

Requirements
Must have
• look elegant, sophisticated. Must have my new logo! My logo is attached as one of the files. It's a headphone logo.

```html
<!DOCTYPE html>
<html lang="en">
<head>
<meta charset="utf-8">
<title>Velvetline Productions – Wedding DJ &amp; Lighting Postcard</title>
<link rel="stylesheet" href="https://fonts.googleapis.com/css2?family=Exo+2:ital,wght@0,400;0,600;1,500;1,600&family=Great+Vibes&family=Titillium+Web:wght@400;600&display=swap">
<style>
  :root {
    --stage: #4a3222;
    --ink: #141414;
    --ink-soft: #1d1d1f;
    --red: #c8201f;
    --red-deep: #8e1414;
    --white: #ffffff;
    --grey: #d6d6d6;
    --violet: #5b2a78;
    --violet-deep: #24102f;
    --amber: #8a4a2a;
  }
  * { box-sizing: border-box; margin: 0; padding: 0; }
  html, body { width: 1200px; height: 1000px; overflow: hidden; }
  body { background: var(--stage); position: relative; font-family: "Exo 2", sans-serif; color: var(--white); }

  .card { position: absolute; width: 601px; height: 465px; background: var(--ink); overflow: hidden; box-shadow: 0 6px 18px rgba(0,0,0,.45); }
  .card--front { left: 33px; top: 25px; }
  .card--back { left: 557px; top: 510px; }

  .photo { position: absolute; }
  .front-photo { left: 0; top: 0; width: 601px; height: 340px;
    background: radial-gradient(ellipse at 62% 40%, #d9c8c0 0%, #7a4f6e 18%, var(--violet) 42%, var(--violet-deep) 80%); }
  .card-shapes { position: absolute; left: 0; top: 0; }

  .brand { position: absolute; display: flex; align-items: center; gap: 8px; }
  .brand-dot { width: 14px; height: 14px; border-radius: 50%; background: var(--red); }
  .brand-name { font-family: "Exo 2", sans-serif; font-weight: 600; font-size: 22px; color: var(--white); letter-spacing: .5px; }
  .card--front .brand { left: 48px; top: 82px; }
  .tagline { position: absolute; left: 28px; top: 131px; font-style: italic; font-weight: 500; font-size: 17px; }

  .services { position: absolute; left: 27px; top: 311px; list-style: none; }
  .services li { font-style: italic; font-weight: 500; font-size: 17px; line-height: 24.2px; display: flex; align-items: center; gap: 7px; }
  .services svg { flex: none; }

  .divider { position: absolute; left: 302px; top: 330px; height: 100px; border-left: 1px dotted #9a9a9a; }
  .motto { position: absolute; left: 322px; top: 368px; }
  .motto-lead { font-family: "Titillium Web", sans-serif; font-size: 21px; line-height: 24px; text-align: right; width: 98px; }
  .motto-script { position: absolute; left: 98px; top: -20px; font-family: "Great Vibes", cursive; font-size: 66px; line-height: 1; white-space: nowrap; }

  .back-photo { left: 0; top: 0; width: 601px; height: 275px;
    background: linear-gradient(170deg, #4b2d5e 0%, #6b3a4a 35%, var(--amber) 65%, #3a1e22 100%); }
  .section-title { position: absolute; left: 34px; top: 28px; font-style: italic; font-weight: 600; font-size: 18px; }
  .inset { position: absolute; border: 4px solid var(--white); box-shadow: 0 3px 8px rgba(0,0,0,.5); }
  .inset-photo { width: 100%; height: 100%; }
  .inset-label { position: absolute; font-weight: 600; font-size: 17px; color: var(--white); text-shadow: 0 1px 3px rgba(0,0,0,.7); }
  .inset--pinspot { left: 376px; top: 20px; width: 200px; height: 146px; transform: rotate(2deg); }
  .inset--pinspot .inset-photo { background: radial-gradient(circle at 50% 45%, #e8d6e6 0%, #8a67b8 25%, #3c2a6e 75%); }
  .inset--pinspot .inset-label { left: 6px; bottom: 4px; }
  .inset--monogram { left: 348px; top: 176px; width: 212px; height: 124px; transform: rotate(-2deg); }
  .inset--monogram .inset-photo { background: linear-gradient(180deg, #2c2260 0%, #5a4fb0 45%, #bfb6e8 100%); }
  .inset--monogram .inset-label { left: 20px; bottom: 2px; font-size: 18px; }

  .about { position: absolute; left: 22px; top: 297px; width: 327px; font-family: "Titillium Web", sans-serif; font-size: 10.3px; line-height: 14.6px; color: var(--grey); text-align: justify; }
  .about strong { color: var(--white); font-weight: 600; }
  .about em { color: var(--white); font-style: italic; }

  .card--back .brand { left: 412px; top: 348px; }
  .contact { position: absolute; left: 370px; top: 395px; width: 200px; text-align: center; font-family: "Titillium Web", sans-serif; }
  .contact p { font-size: 12px; line-height: 15.5px; }
  .contact .phone { font-size: 15px; line-height: 22px; }
</style>
</head>
<body>

<section class="card card--front">
  <div class="photo front-photo" role="img" aria-label="Bride and groom sharing their first dance in a purple-lit ballroom with guests seated around them"></div>
  <svg class="card-shapes" width="601" height="465" viewBox="0 0 601 465" aria-hidden="true">
    <path d="M0,258 C140,228 280,250 400,300 C480,330 560,320 601,285 L601,465 L0,465 Z" fill="var(--red-deep)"/>
    <path d="M0,266 C140,238 280,262 400,310 C480,340 560,330 601,295 L601,465 L0,465 Z" fill="var(--red)"/>
    <path d="M0,285 C140,258 280,283 400,330 C480,357 560,348 601,318 L601,465 L0,465 Z" fill="var(--ink)"/>
    <rect x="0" y="443" width="601" height="22" fill="var(--red)"/>
  </svg>

  <div class="brand"><span class="brand-dot"></span><span class="brand-name">Velvetline Productions</span></div>
  <p class="tagline">DJ “Lighting” Audio/Visual</p>

  <ul class="services">
    <li><svg width="13" height="13" viewBox="0 0 13 13"><rect x=".5" y="2.5" width="10" height="10" fill="none" stroke="#fff"/><path d="M2.5,7 L5,9.5 L12,1" fill="none" stroke="#fff" stroke-width="1.6"/></svg>DJ &amp; Emcee Entertainment</li>
    <li><svg width="13" height="13" viewBox="0 0 13 13"><rect x=".5" y="2.5" width="10" height="10" fill="none" stroke="#fff"/><path d="M2.5,7 L5,9.5 L12,1" fill="none" stroke="#fff" stroke-width="1.6"/></svg>Customised Lighting Decor</li>
    <li><svg width="13" height="13" viewBox="0 0 13 13"><rect x=".5" y="2.5" width="10" height="10" fill="none" stroke="#fff"/><path d="M2.5,7 L5,9.5 L12,1" fill="none" stroke="#fff" stroke-width="1.6"/></svg>Event Hosting &amp; Co-ordination</li>
    <li><svg width="13" height="13" viewBox="0 0 13 13"><rect x=".5" y="2.5" width="10" height="10" fill="none" stroke="#fff"/><path d="M2.5,7 L5,9.5 L12,1" fill="none" stroke="#fff" stroke-width="1.6"/></svg>Helpful Planning Tools</li>
    <li><svg width="13" height="13" viewBox="0 0 13 13"><rect x=".5" y="2.5" width="10" height="10" fill="none" stroke="#fff"/><path d="M2.5,7 L5,9.5 L12,1" fill="none" stroke="#fff" stroke-width="1.6"/></svg>Personlized Service</li>
  </ul>

  <div class="divider"></div>
  <div class="motto">
    <p class="motto-lead">Celebrate with</p>
    <p class="motto-script">Style</p>
  </div>
</section>

<section class="card card--back">
  <div class="photo back-photo" role="img" aria-label="Wedding guests dancing in a circle around the bride on a warm-lit dance floor"></div>
  <svg class="card-shapes" width="601" height="465" viewBox="0 0 601 465" aria-hidden="true">
    <path d="M0,258 L601,222 L601,465 L0,465 Z" fill="var(--red)"/>
    <path d="M0,272 L601,236 L601,465 L0,465 Z" fill="var(--ink)"/>
  </svg>
  <p class="section-title">DJ Entertainment</p>

  <figure class="inset inset--pinspot">
    <div class="inset-photo" role="img" aria-label="Reception table with a floral centrepiece lit by a pinspot in purple light"></div>
    <figcaption class="inset-label">Pinspot Lighting</figcaption>
  </figure>
  <figure class="inset inset--monogram">
    <div class="inset-photo" role="img" aria-label="Ballroom dance floor with a projected couple's monogram under blue uplighting"></div>
    <figcaption class="inset-label">Monogram</figcaption>
  </figure>

  <p class="about">
    <strong>Velvetline Productions</strong> will provide your wedding with <strong>superior sound, brilliant lighting and professional DJ entertainment</strong> to create a memorable experience.<br>
    We know planning your big day can be a little overwhelming. You have to coordinate with so many different people along the way. With our services, we'll make sure you have one less thing to worry about. We've got you covered from the moment you arrive to your final farewell.<br>
    With years of entertainment and production experience, we make sure your occasion comes to life for you and your guests. After all, <strong>its your day, your event and your memories</strong>...<em>its about you</em>
  </p>

  <div class="brand"><span class="brand-dot"></span><span class="brand-name">Velvetline</span></div>
  <div class="contact">
    <p>velvetlinepros.com</p>
    <p>hello@velvetlinepros.com</p>
    <p class="phone">888-555-0142</p>
  </div>
</section>

</body>
</html>
```